依頼詳細
■ デザイン

期間限定のキャンペーンメニュー(縦)です。

印刷掲示・印刷物配布・HPで使用します。

ファスティング(断食)をするためのリゾートホテルの宿泊客へむけたキャンペーンです。

テーマは、健康、デトックス、ダイエット、美しくなる

メインターゲットは、健康志向が高い女性、30歳~60歳

文字は大きく(50歳代が裸眼で見えるサイズ)

■使用する場所
ホテル内フロント・アロマルームで印刷物にラミネートをかけて掲示します
客室インフォメーションブックで印刷物を掲示します
HPに掲載します

■ 納品ファイル
JPG ai PDF

■添付ファイル
キャンペーン企画書
イメージ画像(必ずしも本画像が必須というわけではありません。お手持ちなどがありましたらご提案ください。)

■デザイン納期
4月上旬予定

■画像
お手持ちのものなど、無償使用できる画像でご提案ください。
場合により弊社所有の画像への入れ替えを提案することがあります。

■最下段には、2パターン店舗情報を記入してください。

■詳しくは企画書をご覧ください。ご不明点はメールでお問い合わせください

記載項目
サイズ
A4
ページ数
片面
希望イメージ
シンプル 複雑
単色 カラフル
暗い 明るい
日常 高級
遊び心 厳粛
未来的 伝統的
女性的 男性的
納品ファイル
• 高解像度JPG (.jpg)
• イラストレーター形式 (.ai)
■ 選んだ理由

本キャンペーンのイメージと、メニューの両方がとてもわかりやすく表現されていました。
1、2つのメニューの見やすい色と配置。
2、年齢層高い方にも文字サイズがほどよい。
3、本企画のテーマが表現されている。
4、季節感が感じられる。
5、シンプルななかにも柑橘が香り立つように盛り込まれている。
などが決め手となりました。

■ 提案者全員のお礼・コメント

この度は弊社コンペに多数ご応募くださいましてありがとうございました。とても素晴らしい作品が多く選出にはとても苦労をしました。また引き続きよろしくお願いいたします。

```html
<!DOCTYPE html>
<html lang="ja">
<head>
<meta charset="utf-8">
<title>爽健アロマデトックス キャンペーンメニュー</title>
<link rel="stylesheet" href="https://fonts.googleapis.com/css2?family=Shippori+Mincho:wght@500;700;800&family=Noto+Serif+JP:wght@400;600&display=swap">
<style>
:root{
  --green-deep:#3d7f3a;
  --green-soft:#cfe6b4;
  --green-pale:#eef6e3;
  --orange:#e8852a;
  --orange-soft:#f4b56a;
  --orange-band:#f2a04a;
  --ink:#3a3a3a;
  --paper:#ffffff;
}
*{margin:0;padding:0;box-sizing:border-box}
html,body{width:854px;height:1200px;overflow:hidden;background:var(--paper)}
body{font-family:"Noto Serif JP",serif;color:var(--ink);position:relative}
.hero-photo{position:absolute;left:0;top:0;width:854px;height:600px;
  background:radial-gradient(ellipse at 70% 35%,#f6e3d6 0%,#f2d5c3 25%,#e9eedd 55%,#ffffff 85%),
  linear-gradient(180deg,#dcefc4 0%,#ffffff 100%);}
.hero-photo::after{content:"";position:absolute;inset:0;
  background:linear-gradient(180deg,rgba(255,255,255,0) 60%,#fff 100%),
  radial-gradient(circle at 8% 6%,rgba(172,214,120,.55),transparent 22%),
  radial-gradient(circle at 92% 4%,rgba(172,214,120,.45),transparent 18%);}
.title{position:absolute;left:70px;top:135px;font-family:"Shippori Mincho",serif;font-weight:800;
  color:var(--green-deep);font-size:82px;line-height:96px;letter-spacing:4px}
.lead{position:absolute;left:30px;top:528px;width:800px;font-family:"Shippori Mincho",serif;font-weight:700;
  color:var(--orange);font-size:20px;line-height:34px;letter-spacing:0;white-space:nowrap}
.menu{position:absolute;top:616px;width:390px;height:392px;border:3px solid var(--orange-soft);padding:26px 22px 0}
.menu--left{left:28px}.menu--right{left:434px}
.menu__name{font-family:"Shippori Mincho",serif;font-weight:700;color:var(--orange);font-size:30px;
  border-bottom:2px solid var(--orange-soft);padding-bottom:8px;margin-bottom:12px}
.menu__desc{font-size:15px;line-height:24px;margin-bottom:14px}
.price-list{list-style:none;font-family:"Shippori Mincho",serif;font-weight:500;font-size:25px;line-height:38px}
.price-list li{display:flex;justify-content:space-between;padding:0 30px 0 4px}
.menu__note{font-size:11.5px;line-height:18px;margin-top:14px;color:#555}
.promo-band{position:absolute;left:28px;top:1018px;width:798px;height:40px;background:var(--orange-band);
  color:#fff;font-family:"Shippori Mincho",serif;font-weight:700;font-size:21px;
  display:flex;align-items:center;justify-content:center;gap:24px}
.footer{position:absolute;left:0;top:1064px;width:854px;height:136px;
  background:linear-gradient(90deg,var(--green-pale),#f8fbf2 50%,var(--green-soft));}
.footer__leaves{position:absolute;inset:0}
.contact-box{position:absolute;left:32px;top:1082px;width:380px;height:100px;background:rgba(255,255,255,.85);
  border-radius:16px;padding:16px 20px;font-family:"Shippori Mincho",serif;font-weight:700;color:var(--green-deep)}
.contact-box p{font-size:20px;line-height:34px}
.room-info{position:absolute;left:470px;top:1086px;font-family:"Shippori Mincho",serif;font-weight:700;
  color:var(--green-deep);font-size:20px;line-height:32px}
</style>
</head>
<body>
<div class="hero-photo" role="img" aria-label="アロマトリートメントを受けてくつろぐ女性と柑橘の若葉の写真"></div>

<h1 class="title">爽健<br>アロマ<br>デトックス</h1>

<p class="lead">伊豆特産ダイダイとグレープフルーツオイルで<br>滞った毒素を分解して、リンパ活性トリートメントでデトックスをうながします</p>

<section class="menu menu--left">
  <h2 class="menu__name">利尿デトックスボディ</h2>
  <p class="menu__desc">むくみや冷え性を解消させるために<br>余分な水分の排出をサポートします</p>
  <ul class="price-list">
    <li><span>45 分</span><span>¥6,300-</span></li>
    <li><span>60 分</span><span>¥8,470-</span></li>
    <li><span>90 分</span><span>¥12,540-</span></li>
    <li><span>120 分</span><span>¥15,730-</span></li>
  </ul>
  <p class="menu__note">グレープフルーツオイルに含まれる成分が<br>余分な水分の排出を促します。<br>巡りを整え体内をすっきりさせます。</p>
</section>

<section class="menu menu--right">
  <h2 class="menu__name">爽快デトックスボディ</h2>
  <p class="menu__desc">腸を活性化することで、老廃物の<br>排出力を高めます</p>
  <ul class="price-list">
    <li><span>45 分</span><span>¥6,300-</span></li>
    <li><span>60 分</span><span>¥8,470-</span></li>
    <li><span>90 分</span><span>¥12,540-</span></li>
    <li><span>120 分</span><span>¥15,730-</span></li>
  </ul>
  <p class="menu__note">伊豆ダイダイの爽快な香りが腸を刺激して活性化。<br>ペパーミントとの相乗効果で<br>デトックスをサポートします。</p>
</section>

<div class="promo-band"><span>前日までのご予約なら</span><span>事前割¥500割引します</span><span>60分以上限定です</span></div>

<footer class="footer">
  <svg class="footer__leaves" width="854" height="136" viewBox="0 0 854 136" aria-hidden="true">
    <ellipse cx="820" cy="20" rx="60" ry="34" fill="#b8dc92" opacity=".5"/>
    <ellipse cx="440" cy="120" rx="90" ry="30" fill="#cfe6b4" opacity=".6"/>
  </svg>
</footer>
<div class="contact-box">
  <p>お問い合わせはフロントで承ります</p>
  <p>【全コース男女とも施術できます】</p>
</div>
<div class="room-info">
  <p>アロマルーム / 東館1階にございます</p>
  <p>営業時間：15:00〜22:00</p>
  <p>受付時間：15:00〜18:00</p>
</div>
</body>
</html>
```